Bramwell Resources Ltd. - Refreshed business card challenge

A revised, refreshed business card design for my oil and gas company using my existing logo. Feel free to be as creative as you like!

Target Market(s)

bankers, lawyers

Industry/Entity Type

Oil And Gas Exploration

Contact Information for Business Card

See the "Must Haves" section

Font styles to use
Serif
Sans Serif

Colors

Designer to choose colors to be used in the design.

Requirements
Must have
• Existing business logo, name, title, email, phone number, business address
• Neil Hadley, CA, CPA
• Vice President Finance & Chief Financial Officer
• nhadley@bramwellresources-mail.com
• office: (587)555-0142
• cell: (403)555-0187
• 1400, 815 4 Street S.W.
• Calgary, AB
• T2P 4K8
Should not have
• Should not be plain and boring.

```html
<!DOCTYPE html>
<html lang="en">
<head>
<meta charset="utf-8">
<title>Bramwell Resources – Business Card</title>
<link href="https://fonts.googleapis.com/css2?family=Open+Sans:wght@400;600;700;800&display=swap" rel="stylesheet">
<style>
  :root {
    --forest: #0b4a31;
    --earth: #4e2913;
    --paper: #ffffff;
    --backdrop: #f3f3f3;
    --ink-light: #ffffff;
  }
  * { margin: 0; padding: 0; box-sizing: border-box; }
  html, body {
    width: 1200px;
    height: 800px;
    overflow: hidden;
  }
  body {
    background: var(--backdrop);
    position: relative;
    font-family: "Open Sans", Arial, sans-serif;
  }
  .card {
    position: absolute;
    top: 271px;
    width: 450px;
    height: 257px;
    border-radius: 12px;
    overflow: hidden;
  }
  .card--front { left: 131px; }
  .card--back { left: 620px; }
  .card__art {
    position: absolute;
    inset: 0;
    width: 450px;
    height: 257px;
    display: block;
  }
  .brand {
    position: absolute;
    color: var(--forest);
    font-weight: 800;
    line-height: 1;
    text-align: left;
  }
  .brand__name { font-size: 30px; letter-spacing: -0.5px; display: block; }
  .brand__sub { font-size: 8px; letter-spacing: 1.4px; display: block; margin-top: 3px; text-align: right; }
  .card--front .brand { left: 64px; top: 170px; }
  .card--back .brand { left: 152px; top: 170px; }

  .holder {
    position: absolute;
    right: 29px;
    top: 35px;
    text-align: right;
    color: var(--ink-light);
    white-space: nowrap;
  }
  .holder__name { font-size: 14px; font-weight: 600; letter-spacing: 0.2px; }
  .holder__title { font-size: 7.5px; font-weight: 600; line-height: 12px; margin-top: 4px; }

  .contact {
    position: absolute;
    left: 245px;
    top: 144px;
    list-style: none;
    color: var(--ink-light);
    font-size: 10.5px;
    font-weight: 600;
  }
  .contact li {
    display: flex;
    align-items: center;
    height: 16px;
    white-space: nowrap;
  }
  .contact .contact__email { font-size: 9.2px; letter-spacing: -0.1px; }
  .contact .icon {
    width: 9px;
    height: 9px;
    margin-right: 9px;
    flex: none;
  }
  .contact .indent { padding-left: 18px; }
</style>
</head>
<body>

  <section class="card card--front">
    <svg class="card__art" viewBox="0 0 450 257" aria-hidden="true">
      <rect width="450" height="257" fill="var(--earth)"/>
      <polygon points="0,0 56,0 0,78" fill="var(--forest)"/>
      <polygon points="0,212 0,257 42,257" fill="var(--forest)"/>
      <path d="M0 78 L56 0 L98 0 L148 0 L170 0 C205 40 240 90 238 150 C236 210 200 245 160 257 L42 257 L0 212 Z"
            fill="var(--paper)" stroke="var(--forest)" stroke-width="4"/>
      <path d="M100 -2 C100 30 95 50 98 75 C100 95 112 104 123 104 C135 104 147 95 148 75 C150 50 145 30 146 -2 Z"
            fill="var(--earth)" stroke="var(--forest)" stroke-width="4"/>
    </svg>
    <div class="brand">
      <span class="brand__name">Bramwell</span>
      <span class="brand__sub">RESOURCES</span>
    </div>

    <div class="holder">
      <p class="holder__name">Neil Hadley, CA, CPA</p>
      <p class="holder__title">Vice President Finance<br>&amp; Chief Financial Officer</p>
    </div>

    <ul class="contact">
      <li>
        <svg class="icon" viewBox="0 0 10 10"><rect x="0.5" y="2" width="9" height="6.5" fill="#fff"/><path d="M0.5 2 L5 6 L9.5 2" fill="none" stroke="var(--earth)" stroke-width="1"/></svg>
        <span class="contact__email">nhadley@bramwellresources-mail.com</span>
      </li>
      <li>
        <svg class="icon" viewBox="0 0 10 10"><path d="M1 3.5 Q5 0.5 9 3.5 L8 5 L6.5 4.2 V3.3 Q5 2.8 3.5 3.3 V4.2 L2 5 Z" fill="#fff"/><rect x="2" y="5.5" width="6" height="3.5" rx="0.8" fill="#fff"/></svg>
        office: (587)555-0142
      </li>
      <li>
        <svg class="icon" viewBox="0 0 10 10"><circle cx="5" cy="5" r="4.6" fill="#fff"/><path d="M3.6 2.6 L4.6 3.8 L4 4.5 Q4.6 5.8 5.6 6.2 L6.3 5.5 L7.4 6.5 L6.6 7.5 Q3.2 6.8 2.6 3.4 Z" fill="var(--earth)"/></svg>
        cell: (403)555-0187
      </li>
      <li>
        <svg class="icon" viewBox="0 0 10 10"><path d="M5 0.5 A3.3 3.3 0 0 1 8.3 3.8 C8.3 6 5 9.5 5 9.5 C5 9.5 1.7 6 1.7 3.8 A3.3 3.3 0 0 1 5 0.5 Z" fill="#fff"/><circle cx="5" cy="3.8" r="1.3" fill="var(--earth)"/></svg>
        1400, 815 4 Street S.W.
      </li>
      <li class="indent">Calgary, AB</li>
      <li class="indent">T2P 4K8</li>
    </ul>
  </section>

  <section class="card card--back">
    <svg class="card__art" viewBox="0 0 450 257" aria-hidden="true">
      <rect width="450" height="257" fill="var(--earth)"/>
      <rect width="180" height="257" fill="var(--forest)"/>
      <path d="M178 0 L300 0 C360 60 395 120 385 180 C375 230 330 257 290 257 L195 257 C150 257 105 225 100 175 C95 115 130 60 178 0 Z"
            fill="var(--paper)" stroke="var(--forest)" stroke-width="4"/>
      <path d="M232 -2 C232 30 227 50 230 75 C232 95 244 104 255 104 C267 104 279 95 280 75 C282 50 277 30 278 -2 Z"
            fill="var(--earth)" stroke="var(--forest)" stroke-width="4"/>
    </svg>
    <div class="brand">
      <span class="brand__name">Bramwell</span>
      <span class="brand__sub">RESOURCES</span>
    </div>
  </section>

</body>
</html>
```